Design a BOLD Ad Design for Fitness Club

We are fitness facility that is about to run our new "Bright Parent Reboot" program and we need a bold design created for an ad that will run on Instagram and Facebook.

The ad needs to be eye catching, easy to read and attractive so that someone stops scrolling and clicks to join.

The add needs to be sized to 1080 x 1080, include our logo and the text "Bright Parent Reboot" and "Starting September 23rd"

I have included an example photo, which is to be used as an example only of a design style that stands out to us, (colors, female photo style, etc)

I have also included our logo, which the yellow color can be changed for this design.

Thank you and we look forward to seeing your design.

```html
<!DOCTYPE html>
<html lang="en">
<head>
<meta charset="utf-8">
<title>PeakForma – Bright Parent Reboot</title>
<link rel="stylesheet" href="https://fonts.googleapis.com/css2?family=Anton&family=Montserrat:wght@500;700;800;900&family=Oswald:wght@500;700&display=swap">
<style>
  :root {
    --yellow: #f7cf0a;
    --white: #ffffff;
    --ink: #15171a;
    --charcoal: #24272c;
    --slate: #3a3f47;
    --gym-teal: #2c4a52;
    --skin: #b98a64;
    --silver: #c9c9c9;
  }
  * { margin: 0; padding: 0; box-sizing: border-box; }
  html, body { width: 1200px; height: 1200px; overflow: hidden; background: var(--ink); }
  .ad {
    position: relative;
    width: 1200px; height: 1200px;
    overflow: hidden;
    font-family: "Montserrat", sans-serif;
    color: var(--white);
  }
  .ad__photo {
    position: absolute; inset: 0;
    background:
      radial-gradient(ellipse 240px 420px at 570px 700px, rgba(185,138,100,.75), rgba(185,138,100,0) 70%),
      radial-gradient(ellipse 500px 300px at 180px 360px, rgba(44,74,82,.55), rgba(44,74,82,0) 70%),
      radial-gradient(ellipse 140px 60px at 80px 640px, rgba(255,170,20,.55), rgba(255,170,20,0) 70%),
      radial-gradient(ellipse 120px 60px at 1080px 820px, rgba(255,150,20,.5), rgba(255,150,20,0) 70%),
      linear-gradient(180deg, #1a1c1f 0%, #2a2b2d 45%, #1e1f21 100%);
  }
  .ad__footer-band {
    position: absolute; left: 0; right: 0; bottom: 0; height: 150px;
    background: linear-gradient(180deg, rgba(58,63,71,.85), var(--slate));
  }

  .brand {
    position: absolute; left: 0; right: 0; top: 46px;
    text-align: center;
    font-family: "Anton", sans-serif;
    font-size: 150px; line-height: 1;
    color: var(--white);
    letter-spacing: -2px;
  }
  .tagline {
    position: absolute; left: 0; right: 0; top: 284px;
    display: flex; justify-content: center; align-items: center; gap: 14px;
    font-weight: 800; font-size: 17px; letter-spacing: 4px;
    color: var(--yellow);
  }
  .tagline svg { width: 22px; height: 22px; }

  .social {
    position: absolute; left: 990px; top: 40px; width: 140px; text-align: center;
  }
  .social__label { font-weight: 700; font-size: 12.5px; letter-spacing: .5px; }
  .social__dots { display: flex; justify-content: center; gap: 9px; margin-top: 12px; }
  .social__dots span { width: 20px; height: 20px; border-radius: 50%; background: var(--yellow); }

  .start { position: absolute; left: 92px; top: 280px; width: 283px; text-align: center; }
  .start__label { font-weight: 900; font-size: 24px; letter-spacing: 1.5px; color: var(--yellow); }
  .start__pill {
    margin-top: 22px; height: 146px;
    border: 2px solid var(--yellow); border-radius: 60px;
    background: rgba(20,20,22,.35);
    display: flex; flex-direction: column; justify-content: center; align-items: center;
    color: var(--silver);
  }
  .start__day { font-family: "Anton", sans-serif; font-size: 64px; line-height: .95; }
  .start__month { font-weight: 900; font-size: 26px; letter-spacing: -1px; }

  .headline { position: absolute; font-family: "Anton", sans-serif; line-height: 1; }
  .headline--one { left: 470px; top: 352px; font-size: 176px; }
  .headline--two { left: 400px; top: 560px; font-size: 200px; }
  .headline--three {
    left: 386px; top: 770px; font-family: "Montserrat", sans-serif;
    font-weight: 900; font-style: italic; font-size: 96px; letter-spacing: -5px;
  }
  .is-white { color: var(--white); }
  .is-yellow { color: var(--yellow); }

  .pitch {
    position: absolute; left: 82px; top: 876px; width: 300px;
    font-family: "Oswald", sans-serif; font-weight: 500; font-style: italic;
    font-size: 30px; line-height: 1.02; text-transform: uppercase;
    transform: rotate(-3deg); transform-origin: left top;
  }
  .pitch__accent { color: var(--yellow); font-weight: 700; font-size: 38px; }
  .pitch__big { font-size: 38px; }

  .challenge { position: absolute; left: 376px; top: 920px; width: 400px; text-align: center; }
  .challenge__lead { font-weight: 800; font-size: 18px; letter-spacing: .3px; }
  .challenge__main { font-weight: 900; font-size: 44px; color: var(--yellow); line-height: 1.05; letter-spacing: -1px; }

  .cta {
    position: absolute; left: 368px; top: 1044px; width: 420px; height: 96px;
    border: 2px solid var(--white); border-radius: 48px;
    display: flex; align-items: center; justify-content: center;
  }
  .cta::before {
    content: ""; position: absolute; inset: 8px;
    border: 1px dashed rgba(255,255,255,.6); border-radius: 40px;
  }
  .cta__text { display: flex; align-items: center; gap: 12px; font-weight: 900; font-size: 46px; letter-spacing: -2px; }
  .cta__text svg { width: 26px; height: 26px; }

  .contact { position: absolute; left: 52px; top: 1072px; }
  .contact__label { font-weight: 500; font-size: 17px; margin-left: 10px; }
  .contact__phone { font-weight: 800; font-size: 26px; letter-spacing: 2px; margin-top: 2px; }

  .website {
    position: absolute; right: 66px; top: 1098px;
    font-weight: 700; font-size: 17.5px; color: var(--yellow);
  }
</style>
</head>
<body>
<main class="ad">
  <div class="ad__photo" role="img" aria-label="Smiling athletic woman in a grey sports top standing hands on hips in a dark gym, with blurred orange dumbbells floating on both sides"></div>
  <div class="ad__footer-band"></div>

  <h1 class="brand">PeakForma</h1>

  <p class="tagline">
    <svg viewBox="0 0 22 22" aria-hidden="true"><rect x="3" y="4" width="3" height="14" fill="#fff"/><rect x="8" y="2" width="3" height="18" fill="#fff"/><rect x="13" y="10" width="9" height="2" fill="#fff"/></svg>
    PERSONAL GROUP TRAINING
    <svg viewBox="0 0 22 22" aria-hidden="true"><rect x="0" y="10" width="9" height="2" fill="#fff"/><rect x="11" y="2" width="3" height="18" fill="#fff"/><rect x="16" y="4" width="3" height="14" fill="#fff"/></svg>
  </p>

  <div class="social">
    <p class="social__label">FOLLOW US NOW</p>
    <div class="social__dots" aria-hidden="true"><span></span><span></span><span></span><span></span></div>
  </div>

  <div class="start">
    <p class="start__label">STARTING</p>
    <div class="start__pill">
      <span class="start__day">23RD</span>
      <span class="start__month">SEPTEMBER</span>
    </div>
  </div>

  <h2 class="headline-group">
    <span class="headline headline--one"><span class="is-white">BRI</span><span class="is-yellow">GHT</span></span>
    <span class="headline headline--two"><span class="is-yellow">PAR</span><span class="is-white">ENT</span></span>
    <span class="headline headline--three"><span class="is-white">REB</span><span class="is-yellow">OOT</span></span>
  </h2>

  <p class="pitch">
    Transform your body<br>&amp; your mind with<br>
    <span class="pitch__accent">Our personal</span><br>
    <span class="pitch__big">Group training</span>
  </p>

  <div class="challenge">
    <p class="challenge__lead">GET THE CHALLENGE FOR YOUR</p>
    <p class="challenge__main">STRONG BODY</p>
  </div>

  <a class="cta">
    <span class="cta__text">
      <svg viewBox="0 0 26 26" aria-hidden="true"><path d="M3 13h19M14 5l8 8-8 8" fill="none" stroke="#fff" stroke-width="2.5"/></svg>
      JOIN NOW
    </span>
  </a>

  <div class="contact">
    <p class="contact__label">FOR MORE DETAILS</p>
    <p class="contact__phone">+1 555-014-2290</p>
  </div>

  <p class="website">www.joinpeakforma.com</p>
</main>
</body>
</html>
```